依頼詳細
スパ(ラポルト ミルネ表参道)のお客様向けのDMの作成をお願いいたします。
シンプルで洗練されたデザインでお願いいたします。期間限定の特別トリートメントの訴求です。写真のイメージに合わせたテイストでお願いします。

文字が多いのですが、すっきりと分かりやすくしていただけると幸いです。

本依頼の際に画像の本データは送付いたします。
記載項目
中面:プロモーション内容
宛名面:告知文
希望イメージ
シンプル 複雑
単色 カラフル
暗い 明るい
日常 高級
遊び心 厳粛
未来的 伝統的
女性的 男性的
希望する色
写真に合わせてゴールドを中心に、プラスするなら深いグリーンをでお願いします
納品ファイル
• 高解像度JPG (.jpg)
• イラストレーター形式 (.ai)
補足説明

ブランドのイメージにあったため当選させていただきました。

沢山のご応募ありがとうございました。引き続きどうぞよろしくお願いいたします。

```html
<!DOCTYPE html>
<html lang="ja">
<head>
<meta charset="utf-8">
<title>タイガ ヒーリング スパプログラム</title>
<link rel="stylesheet" href="https://fonts.googleapis.com/css2?family=Shippori+Mincho:wght@400;500;600&family=Noto+Serif+JP:wght@400;500&display=swap">
<style>
  :root {
    --gold: #c9a35c;
    --gold-light: #dcc08a;
    --forest: #17261e;
    --forest-deep: #101c16;
    --ivory: #f3ece0;
    --ivory-soft: #d9d2c5;
  }
  * { margin: 0; padding: 0; box-sizing: border-box; }
  html, body { width: 813px; height: 1200px; overflow: hidden; background: var(--forest-deep); }
  .flyer {
    position: relative;
    width: 813px;
    height: 1200px;
    overflow: hidden;
    font-family: "Shippori Mincho", "Noto Serif JP", serif;
    color: var(--ivory);
    background: var(--forest);
  }
  .hero-photo {
    position: absolute;
    left: 0; top: 0;
    width: 813px; height: 900px;
    background:
      radial-gradient(ellipse 300px 220px at 640px 210px, rgba(246,220,170,0.55), rgba(246,220,170,0) 70%),
      radial-gradient(ellipse 520px 260px at 300px 640px, rgba(196,140,100,0.75), rgba(120,80,55,0) 75%),
      radial-gradient(ellipse 260px 180px at 130px 260px, rgba(120,100,70,0.5), rgba(0,0,0,0) 70%),
      linear-gradient(180deg, #3c3025 0%, #4a3a2c 35%, #5a4333 60%, #2a2119 88%, var(--forest) 100%);
  }
  .season {
    position: absolute;
    left: 42px; top: 36px;
    color: var(--gold-light);
  }
  .season-year { font-size: 27px; font-weight: 500; letter-spacing: 0.04em; }
  .season-start { margin-top: 14px; font-size: 21px; font-weight: 500; letter-spacing: 0.03em; }
  .lead {
    position: absolute;
    left: 42px; top: 172px;
    font-size: 18px;
    line-height: 1.62;
    letter-spacing: 0.05em;
    color: var(--ivory);
  }
  .program-title {
    position: absolute;
    top: 220px; right: 70px;
    writing-mode: vertical-rl;
    font-size: 62px;
    font-weight: 500;
    line-height: 1.3;
    letter-spacing: 0.12em;
    color: #fff;
    text-shadow: 0 0 14px rgba(0,0,0,0.35);
  }
  .menu {
    position: absolute;
    left: 0; top: 878px;
    width: 813px; height: 322px;
    padding: 22px 36px 0 40px;
    background: linear-gradient(180deg, rgba(23,38,30,0.92) 0%, var(--forest) 20%, var(--forest-deep) 100%);
    display: grid;
    grid-template-columns: 248px 236px 240px;
    column-gap: 14px;
  }
  .course-name {
    font-size: 15.5px;
    font-weight: 600;
    line-height: 1.45;
    color: var(--gold);
    letter-spacing: 0.02em;
    min-height: 45px;
  }
  .course-name .tier { display: block; padding-left: 52px; }
  .course-price {
    margin-top: 6px;
    font-size: 19px;
    font-weight: 500;
    letter-spacing: 0.02em;
    color: var(--ivory);
  }
  .course-text {
    margin-top: 16px;
    font-family: "Noto Serif JP", serif;
    font-size: 12.5px;
    line-height: 1.72;
    color: var(--ivory-soft);
  }
  .tax-note {
    position: absolute;
    right: 40px; bottom: 18px;
    font-family: "Noto Serif JP", serif;
    font-size: 10px;
    color: var(--ivory-soft);
  }
</style>
</head>
<body>
<main class="flyer">
  <div class="hero-photo" role="img" aria-label="キャンドルオイルを背中に垂らされ、うつ伏せでくつろぐ女性のスパトリートメント写真"></div>

  <header class="season">
    <p class="season-year">2019年冬限定</p>
    <p class="season-start">トリートメント 12/1(日)より</p>
  </header>

  <p class="lead">トリートメントオイルキャンドルで、<br>深い安らぎ、深い森に<br>抱かれているような温もりを</p>

  <h1 class="program-title">タイガ ヒーリング<br>スパプログラム</h1>

  <section class="menu">
    <article class="course">
      <h2 class="course-name">タイガ ホットオイル<br>キャンドルトリートメント</h2>
      <p class="course-price">60分 / 19,800円</p>
      <p class="course-text">「タイガ」とは、ロシア語でシベリア地方の針葉樹林のことであり、樹齢500年にも及ぶ木々が生い茂る、とても神聖な場所。キャンドルから溶け出したオイルの温もりとタイガの香りが深く心地よいボディトリートメントで極上のリラックスタイムへ導きます。</p>
    </article>
    <article class="course">
      <h2 class="course-name">タイガ ホットストーン<br>キャンドルトリートメント</h2>
      <p class="course-price">90分 / 26,400円</p>
      <p class="course-text">キャンドルオイルと自然石を使ったストーンボディセラピー。自然の力と共に癒す極上のリラクゼーショントリートメント。</p>
    </article>
    <article class="course">
      <h2 class="course-name">タイガ ホットオイル<br>キャンドルトリートメント<span class="tier">Premium</span></h2>
      <p class="course-price">120分 / 33,000円</p>
      <p class="course-text">キャンドルトリートメントにエイジングケアフェイシャルをプラス。心と身体の解放と輝く肌へと導く贅沢なコース。</p>
    </article>
    <p class="tax-note">※価格はすべて税込です。</p>
  </section>
</main>
</body>
</html>
```